Save The Date for 2019 QRP Symposium

We have an annual meeting each June and need a Save the Date (STD) designed. It should be a two-sided postcard with room for address and stamp (according to US Mail postal standards). I have attached some examples from prior years, but we would appreciate a more modern and attractive design for this year's STD.

Target Market(s)

Our own members - nurses, nurse practitioners, PAs and physicians

Industry/Entity Type

Medical

Requirements
Must have
• Must include our logos (attached), ideally in a coordinating fashion - as was done in prior years (see examples attached) and without modifying the logos too much. Needs have the following information:
• - "Save the Date"
• - "The 12th Annual Vascular Crew Roundtable"
• - "Friday, June 7, 2019" or "6/7/19"
• - "The Halvern–Trask Building | 274 West 19th Street | NYC"
• - Please include our website (www.zq-olm.example/events), phone number (212-555-0147) and email address (ask@zq-olm.example) for people to ask questions
• - Must have space for a postage stamp and the name/address of the postcard recipient
Nice to have
• Would be nice to remain in our blue/grey/olive color palate (see attached Brand Standards guide).
Should not have
• Please do not use stock photos of medical staff. Please don't use cartoons or cartoon images (although a tasteful sketch may be considered).

```html
<!DOCTYPE html>
<html lang="en">
<head>
<meta charset="utf-8">
<title>Save the Date – 12th Annual Vascular Crew Roundtable</title>
<link rel="stylesheet" href="https://fonts.googleapis.com/css2?family=Bebas+Neue&family=Tinos&family=Open+Sans:wght@400&family=Arimo:wght@400&display=swap">
<style>
  :root {
    --navy: #1b2f5e;
    --navy-soft: #24396b;
    --olive: #b3aa83;
    --white: #ffffff;
    --ink: #333333;
    --badge-blue: #2a6fb0;
    --backdrop: #eceae6;
  }
  * { margin: 0; padding: 0; box-sizing: border-box; }
  html, body { width: 993px; height: 1200px; overflow: hidden; background: var(--backdrop); }
  .canvas { position: relative; width: 993px; height: 1200px; }
  .postcard {
    position: absolute; left: 72px; width: 912px; height: 610px;
    transform: scale(0.93); transform-origin: top left;
    background: var(--white); overflow: hidden;
    box-shadow: 0 3px 10px rgba(0,0,0,0.25);
  }
  .postcard--front { top: 18px; }
  .postcard--back { top: 615px; }
  .card-shapes { position: absolute; inset: 0; }

  /* Front */
  .front-heading { position: absolute; right: 42px; top: 30px; text-align: right; }
  .edition { font-family: "Bebas Neue", sans-serif; font-size: 52px; line-height: 1; color: var(--olive); letter-spacing: 1px; }
  .event-name { font-family: "Tinos", serif; font-size: 35px; color: var(--white); margin-top: 12px; letter-spacing: 0.5px; }
  .save-the-date { font-family: "Bebas Neue", sans-serif; font-size: 136px; line-height: 1; margin-top: 22px; letter-spacing: 2px; color: var(--olive); text-shadow: 0 4px 8px rgba(0,0,0,0.35); }
  .save-the-date .accent { color: var(--white); }
  .venue { font-family: "Tinos", serif; font-size: 25px; line-height: 30px; color: var(--white); margin-top: 20px; }
  .event-date { position: absolute; left: 552px; top: 442px; font-family: "Tinos", serif; font-size: 31px; color: var(--white); letter-spacing: 0.5px; }
  .contact { position: absolute; right: 42px; top: 523px; text-align: right; font-family: "Arimo", sans-serif; font-size: 15px; line-height: 20px; color: var(--ink); }
  .contact .web { color: var(--olive); font-size: 16px; margin-top: 8px; }

  /* Back */
  .org-lockup { position: absolute; left: 29px; top: 28px; display: flex; align-items: center; gap: 22px; }
  .org-mark { width: 104px; height: 104px; border-radius: 50%; border: 3px solid var(--white); }
  .org-name { font-family: "Tinos", serif; font-size: 31px; color: var(--white); }
  .message { position: absolute; left: 29px; top: 178px; width: 390px; font-family: "Open Sans", sans-serif; font-size: 14.5px; line-height: 20.5px; color: var(--white); }
  .message p { margin-bottom: 13px; }
  .message p.spaced { margin-top: 20px; }
  .message .web { color: var(--olive); font-family: "Arimo", sans-serif; font-size: 16px; margin-top: 22px; }
  .return-address { position: absolute; left: 498px; top: 61px; font-family: "Arimo", sans-serif; font-size: 15px; line-height: 19px; color: var(--ink); }
</style>
</head>
<body>
<main class="canvas">

  <section class="postcard postcard--front">
    <svg class="card-shapes" width="912" height="610" viewBox="0 0 912 610">
      <path fill="var(--olive)" d="M0,448 C150,490 330,498 470,470 L480,478 C330,505 140,500 0,466 Z"/>
      <path fill="var(--navy)" d="M0,0 H912 V434 C800,410 650,420 480,460 C350,490 150,482 0,448 Z"/>
      <path fill="var(--white)" d="M470,468 C620,426 790,414 912,434 V442 C790,424 620,438 478,474 Z"/>
      <path fill="var(--olive)" d="M478,474 C620,438 790,424 912,442 V472 C850,498 720,512 640,506 C560,500 510,486 478,474 Z"/>
      <rect role="img" aria-label="Faint anatomical heart sketch" x="20" y="20" width="470" height="420" rx="200" fill="var(--navy-soft)" opacity="0.55"/>
      <circle cx="78" cy="546" r="38" fill="none" stroke="var(--badge-blue)" stroke-width="3"/>
      <circle cx="218" cy="546" r="40" fill="var(--badge-blue)"/>
      <circle cx="360" cy="546" r="40" fill="none" stroke="var(--badge-blue)" stroke-width="3"/>
    </svg>
    <div class="front-heading">
      <div class="edition">12th Annual</div>
      <div class="event-name">VASCULAR CREW ROUNDTABLE</div>
      <div class="save-the-date">Save <span class="accent">The</span> Date</div>
      <div class="venue">The Halvern–Trask Building<br>274 West 19th Street NYC</div>
    </div>
    <div class="event-date">FRIDAY, JUNE 7, 2019</div>
    <div class="contact">
      For additional information call (212) 555-0147<br>
      or email ask@zq-olm.example
      <div class="web">www.zq-olm.example/events</div>
    </div>
  </section>

  <section class="postcard postcard--back">
    <svg class="card-shapes" width="912" height="610" viewBox="0 0 912 610">
      <path fill="var(--olive)" d="M455,0 H478 C494,60 494,200 514,300 C544,420 544,520 506,610 H480 C520,520 520,420 490,300 C470,200 470,60 455,0 Z"/>
      <path fill="var(--navy)" d="M0,0 H455 C470,60 470,200 490,300 C520,420 520,520 480,610 H0 Z"/>
    </svg>
    <div class="org-lockup">
      <div class="org-mark"></div>
      <div class="org-name">Olmstead Heart College</div>
    </div>
    <div class="message">
      <p>Join us for TWO great events at The Lodge at Fernmere in beautiful Canandaigua, New York, this June!</p>
      <p>Now in its tenth year, the Annual Vascular Crew Roundtable (QRP) is a unique all-day academic event designed to enhance current knowledge about the etiology, prevention, intervention and management of cardiovascular disease.</p>
      <p>In the evening, the New York State Chapter of the OHC will host its first-ever Summer Soirée, featuring the band Rex &amp; the Quiet Hours playing us off into the night. A courtesy block of rooms has already been secured at The Lodge for these two events.</p>
      <p class="spaced">To reserve a room at the discounted rate, please call (800) 555-0192 and be sure to mention “The Eastbrook Cardiac Society.”</p>
      <div class="web">www.zq-olm.example/events</div>
    </div>
    <div class="return-address">318 Linden Avenue, Ste. 604<br>New York, NY 10021</div>
  </section>

</main>
</body>
</html>
```